Flyer/Poster Tischtennis Sportverein
Zielgruppe
Tischtennisverein - Zielgruppe: Kinder von 8 - 12 Jahren
Aufgabenstellung
Allgemeiner Flyer für Tischtennisverein - Werbung für Kindertraining, Texbereich sollte im Design enthalten sein, aber so gestaltet dass der Text je nach Bedarf durch uns angepasst werden kann
DIN Format: Sollte als Postkartenformat sowie als DIN A3 oder DIN A2 Poster zu verwenden
Angehängtes Logo einbinden aber nicht zu prominent

```html
<!DOCTYPE html>
<html lang="de">
<head>
<meta charset="utf-8">
<title>Tischtennis Plakat</title>
<link rel="stylesheet" href="https://fonts.googleapis.com/css2?family=Oswald:wght@700&family=Arimo:wght@400;700&display=swap">
<style>
  :root {
    --page-bg: #ffffff;
    --poster-bg: #ffffff;
    --poster-border: #3a3a3a;
    --photo-red: #d8141a;
    --photo-dark: #3a0a0a;
    --headline-grey: #9a9a9a;
    --text-dark: #1a1a1a;
    --footer-grey: #444444;
    --club-red: #d8141a;
  }
  html, body {
    margin: 0;
    width: 1200px;
    height: 800px;
    overflow: hidden;
    background: var(--page-bg);
  }
  .canvas {
    position: relative;
    width: 1200px;
    height: 800px;
  }
  .poster-frame {
    position: absolute;
    left: 338px;
    top: 30px;
    width: 524px;
    height: 740px;
    border: 1px solid var(--poster-border);
    box-sizing: border-box;
    overflow: hidden;
  }
  .poster {
    position: absolute;
    left: 0;
    top: 0;
    width: 554px;
    height: 782px;
    transform: scale(0.9458);
    transform-origin: 0 0;
    background: var(--poster-bg);
  }
  .poster-shapes {
    position: absolute;
    inset: 0;
  }
  .club-name {
    position: absolute;
    left: 348px;
    top: 300px;
    width: 170px;
    text-align: center;
    font-family: "Arimo", Arial, sans-serif;
    font-weight: 700;
    font-size: 17px;
    line-height: 22px;
    color: var(--club-red);
  }
  .headline {
    position: absolute;
    right: 24px;
    top: 404px;
    margin: 0;
    text-align: right;
    font-family: "Oswald", "Arial Narrow", sans-serif;
    font-weight: 700;
    font-size: 80px;
    line-height: 78px;
    letter-spacing: -1.5px;
    color: var(--headline-grey);
  }
  .body-copy {
    position: absolute;
    right: 21px;
    top: 596px;
    width: 420px;
    margin: 0;
    text-align: right;
    font-family: "Arimo", Arial, sans-serif;
    font-weight: 700;
    font-size: 13.6px;
    line-height: 15.4px;
    color: var(--text-dark);
  }
  .footer-line {
    position: absolute;
    right: 32px;
    top: 751px;
    margin: 0;
    font-family: "Arimo", Arial, sans-serif;
    font-weight: 400;
    font-size: 10.5px;
    color: var(--footer-grey);
    white-space: pre;
  }
</style>
</head>
<body>
<div class="canvas">
  <div class="poster-frame">
    <div class="poster">
      <svg class="poster-shapes" viewBox="0 0 554 782" width="554" height="782" aria-hidden="false">
        <defs>
          <linearGradient id="photoTone" x1="0" y1="0" x2="1" y2="1">
            <stop offset="0" stop-color="#e01a1e"/>
            <stop offset="0.45" stop-color="#b01014"/>
            <stop offset="1" stop-color="#2a0808"/>
          </linearGradient>
        </defs>
        <polygon class="photo-band" role="img"
                 aria-label="Foto: Tischtennisspieler beim Aufschlag vor rot getönter Halle"
                 points="0,176 223,0 554,0 554,155 0,701"
                 fill="url(#photoTone)"/>
        <circle class="club-badge" cx="433" cy="323" r="85" fill="#ffffff"/>
      </svg>
      <div class="club-name">SV Lindenbach</div>
      <h1 class="headline">Das nächste<br>Spiel steht an</h1>
      <p class="body-copy">Olor as vellab inis soluptam, et laborum hillam dio. Ut est audic tet, veliassum iliatus simaior recte coris velentione nobissim quae inti­ant ionsequi occusap ediciunt expliquati atiuriatem est, quam sitatisti qui que il ipsum ipsumquae se­quistia as dolest, sandae laboreped milluptae nonseque dolo ipsusam quis solesci enihica borernatenis aut evel illibus aut ratente mpore, ut optatis quaerum eriae nimendi</p>
      <p class="footer-line">SV Lindenbach 1921 e.V. | Am Mühlweg  |  61234 Lindenbach</p>
    </div>
  </div>
</div>
</body>
</html>
```